TCH Business cards

We are a medium sized property company based in London and require a logo, Business card which reflects a professional company and incorporates our catchy name.

Our statement is (Building for the future) we like colours such as royal blue, greens and light browns but will look at anything.

Contact Information for Business Card

Tidecrest Holdings Limited
Unit 4, 3-5 Parbrook Lane
London
SE21 7QX

Web: www.tidecrestholdings.example

Email: tidecrestltd@mailbox.example

Telephone: +44-208-555-0142
Fax: +44-208-555-0187

```html
<!DOCTYPE html>
<html lang="en">
<head>
<meta charset="utf-8">
<title>Tidecrest Holdings Limited – Business Card</title>
<link rel="stylesheet" href="https://fonts.googleapis.com/css2?family=Arimo:wght@400;700&display=swap">
<style>
  :root {
    --paper: #ffffff;
    --card-edge: #c9c9c9;
    --band: #957f66;
    --ink-light: #ffffff;
  }
  html, body {
    margin: 0;
    padding: 0;
    width: 1200px;
    height: 695px;
    overflow: hidden;
    background: var(--paper);
  }
  .business-card {
    position: relative;
    width: 1200px;
    height: 695px;
    font-family: "Arimo", Arial, sans-serif;
    color: var(--ink-light);
  }
  .card-shape {
    position: absolute;
    inset: 0;
  }
  .brand-mark {
    position: absolute;
    left: 470px;
    top: 196px;
    width: 46px;
    height: 46px;
    background: var(--ink-light);
  }
  .brand-name {
    position: absolute;
    margin: 0;
    font-weight: 700;
    font-size: 54px;
    line-height: 1;
    font-variant: small-caps;
    letter-spacing: 0.5px;
    white-space: nowrap;
  }
  .brand-name--line1 { left: 640px; top: 88px; }
  .brand-name--line2 { left: 592px; top: 151px; }
  .brand-name--line3 { left: 544px; top: 214px; }
  .contact-line {
    position: absolute;
    margin: 0;
    font-size: 32px;
    line-height: 1;
    font-weight: 400;
    white-space: nowrap;
  }
  .contact-company { left: 521px; top: 317px; }
  .contact-street  { left: 469px; top: 369px; }
  .contact-city    { left: 418px; top: 419px; }
  .contact-web     { left: 371px; top: 475px; }
  .contact-email   { left: 319px; top: 526px; }
  .contact-phone   { left: 265px; top: 577px; }
  .contact-fax     { left: 221px; top: 628px; }
</style>
</head>
<body>
  <main class="business-card">
    <svg class="card-shape" width="1200" height="695" viewBox="0 0 1200 695" aria-hidden="true">
      <rect x="59.5" y="5.5" width="1092" height="685" fill="var(--paper)" stroke="var(--card-edge)" stroke-width="1.5"/>
      <polygon points="389,5 1151,5 1151,312 829,690 59,690 59,363" fill="var(--band)"/>
    </svg>

    <span class="brand-mark" aria-hidden="true"></span>
    <p class="brand-name brand-name--line1">Tidecrest</p>
    <p class="brand-name brand-name--line2">Holdings</p>
    <p class="brand-name brand-name--line3">Limited</p>

    <p class="contact-line contact-company">Tidecrest Holdings Limited</p>
    <p class="contact-line contact-street">Unit 4, 3-5 Parbrook Lane,</p>
    <p class="contact-line contact-city">London SE21 7QX</p>
    <p class="contact-line contact-web">W: www.tidecrestholdings.example</p>
    <p class="contact-line contact-email">E: tidecrestltd@mailbox.example</p>
    <p class="contact-line contact-phone">T: +44-208-555-0142</p>
    <p class="contact-line contact-fax">F: +44-208-555-0187</p>
  </main>
</body>
</html>
```